Upscale business cards needed for family office

We would like professional business cards created for employees of our family office. Relatively simple and straightforward, but also with a unique element to set them apart. Probably stick with neutral and simple colors that mesh well with the colors in the logo. We need space for the traditional elements, including name, title, address, email/phone number.

Industry/Entity Type

Business

Contact Information for Business Card

Space for name, title, phone number, email, address

```html
<!DOCTYPE html>
<html lang="en">
<head>
<meta charset="utf-8">
<title>H&amp;R Business Card – Owen Mercer</title>
<link rel="stylesheet" href="https://fonts.googleapis.com/css2?family=Arimo:wght@400;700&display=swap">
<style>
  :root {
    --paper: #ffffff;
    --ink: #1f1f1f;
    --accent-blue: #3a6fb8;
    --contact-blue: #1f95c8;
    --muted: #666666;
    --rule: #8a8a8a;
    --pattern-deep: #6fb2d6;
    --pattern-mid: #a9d3e8;
    --pattern-pale: #e3f1f7;
    --mark-grey: #5c6466;
  }
  html, body {
    margin: 0;
    padding: 0;
    overflow: hidden;
    background: var(--paper);
  }
  .card {
    position: relative;
    width: 1200px;
    height: 686px;
    overflow: hidden;
    background: var(--paper);
    font-family: "Arimo", Arial, sans-serif;
  }
  .card__pattern {
    position: absolute;
    left: 0;
    top: 0;
    width: 560px;
    height: 686px;
  }
  .brand {
    position: absolute;
    left: 152px;
    top: 214px;
    width: 223px;
    height: 248px;
    display: flex;
    align-items: center;
    justify-content: center;
    gap: 12px;
    background: var(--paper);
  }
  .brand__square {
    width: 22px;
    height: 22px;
    background: var(--accent-blue);
  }
  .brand__name {
    font-size: 60px;
    font-weight: 400;
    color: var(--mark-grey);
    letter-spacing: 1px;
  }
  .divider {
    position: absolute;
    left: 431px;
    top: 214px;
    width: 2px;
    height: 251px;
    background: var(--rule);
  }
  .details {
    position: absolute;
    left: 489px;
    top: 0;
  }
  .details > * { position: absolute; left: 0; margin: 0; white-space: nowrap; }
  .person-name {
    top: 214px;
    font-size: 46px;
    font-weight: 700;
    letter-spacing: 2.5px;
    color: var(--ink);
    line-height: 1;
  }
  .person-name__last { color: var(--accent-blue); }
  .person-title {
    top: 265px;
    font-size: 30px;
    letter-spacing: 0.8px;
    color: var(--muted);
    line-height: 1;
  }
  .phone, .email {
    font-size: 30px;
    color: var(--contact-blue);
    line-height: 1;
  }
  .phone { top: 338px; }
  .email { top: 380px; }
  .address {
    top: 446px;
    font-size: 21.5px;
    color: var(--muted);
    line-height: 1;
  }
</style>
</head>
<body>
  <div class="card">
    <svg class="card__pattern" viewBox="0 0 560 686" role="img" aria-label="Decorative pattern of soft blue triangles fading to white">
      <defs>
        <linearGradient id="patternFade" x1="0" y1="0" x2="1" y2="0">
          <stop offset="0" stop-color="var(--pattern-deep)"/>
          <stop offset="0.3" stop-color="var(--pattern-mid)"/>
          <stop offset="0.7" stop-color="var(--pattern-pale)"/>
          <stop offset="1" stop-color="#ffffff" stop-opacity="0"/>
        </linearGradient>
        <linearGradient id="patternFadeV" x1="0" y1="0" x2="0" y2="1">
          <stop offset="0" stop-color="#ffffff" stop-opacity="0"/>
          <stop offset="0.55" stop-color="#ffffff" stop-opacity="0.35"/>
          <stop offset="1" stop-color="#ffffff" stop-opacity="0"/>
        </linearGradient>
      </defs>
      <rect width="560" height="686" fill="url(#patternFade)"/>
      <rect width="560" height="686" fill="url(#patternFadeV)"/>
    </svg>

    <div class="brand">
      <span class="brand__square"></span>
      <span class="brand__name">H&amp;R</span>
    </div>

    <div class="divider"></div>

    <div class="details">
      <h1 class="person-name">OWEN <span class="person-name__last">MERCER</span></h1>
      <p class="person-title">Managing Director</p>
      <p class="phone">1-503-555-0142 / 1-688-555-0199</p>
      <p class="email">office@harborreed.com</p>
      <p class="address">H&amp;R Office 2180 NE Alder St Portland, OR 97232</p>
    </div>
  </div>
</body>
</html>
```